BrightvaleCare.com, a web based eHealth startup, needs a URL landing page.

We will be building a portfolio of mocked up website screen shots of our products that we will use to engage prospective customers. We would like to start with the company's URL landing page in order to quickly capture a client's interest and identify a graphic artist that we think has the understanding of the feel/UI we are looking for and the talent to meet our expectations. The two solutions we would like to showcase are "BrightvaleConnectLink" (BCL) and "BrightvaleCircles" (BCS).

BCL is a product for improving hospital inpatient communication using tablets and smart phones. Key descriptors for this solution would be, "Improve communication between the patient, the health care team, and the family care team", "Improve communication between Health Team members", and "Monitor for success and improvement opportunities of administrative goals using direct patient feedback."

BCS is a product for improving patient communication after discharge using tablets, smart phones, and computers. Key descriptors for this solution would be, "Transition support to the Family Care Team", "Stay connected after discharge by creating a VitaCircle of support", and "Monitor progress, provide encouragement, and coordinate support of loved ones"

The goal of the site will be to give potential customers the impression/feeling of great communication, happiness, and health to patients and staff in the hospital and patients, family, and health care providers outside of the hospital. We are hoping to build a relationship with a talented graphic artist as we continue to grow.
Updates

                                        Hello all, I'm trying to upload a logo file to the project brief, but I'm having a little trouble. I have contacted customer service to request a little help. I will also try and find some examples of pages that may have the look I was thinking of. I didn't try to find anything at the start of the project because I was interested to see if there was a design that I may not have thought of. I can certainly try to find some examples though. As for the logo, I tried to put something together on Photoshop, though I also did one on PowerPoint. All I did for now was use BrightvaleCare where the My was in freestyle script, Health was in Adobe Caslon, the e at the end of Health was in freestyle script again, and the Solutions was in Adobe Caslon again. I also made the freestyle script a bright blue and the Adobe Caslon black in color. This was just what I tried first. Underneath the script I had three circles overlapping so that the point at which they all intersected was in the shape of a shield. This symbol stood for "patient centered care". I guess I'll be posting a project for a logo design soon as well to help refine this. This is my first time using a design site like this so I apologize if there is information needed that I have not provided in a easy to use format. I will certainly extend the deadline if more time is needed.  Thank you and please feel free to send any messages or comments. Thanks again.  

Industry/Entity Type

Building

Requirements
Must have
• A banner with scrolling pictures depicting scenes of patients of all ages happily interacting with hospital health team members, people (patients and nurses/doctors) using tablets, smart phones, and computers in the in the hospital, and patients (elderly and 10-15 years old) using happily using a tablet, smart phone, and/or computer.
• Clean, clutter free look.
• Buttons for [Home], [Solutions], [Platform Model], and [Contact Us].

```html
<!DOCTYPE html>
<html lang="en">
<head>
<meta charset="utf-8">
<title>BrightvaleCare.com</title>
<link rel="stylesheet" href="https://fonts.googleapis.com/css2?family=Oswald:wght@300;400;700&family=Arimo:wght@400;700&display=swap">
<style>
  :root {
    --brand-blue: #0a9bd6;
    --brand-blue-light: #19b2e6;
    --brand-blue-deep: #0288c4;
    --navy: #34557f;
    --navy-dark: #2c4a72;
    --text-blue: #0f6fae;
    --title-light: #1f8fc9;
    --footer-bg: #3c5e8b;
    --footer-link: #e6eef8;
    --footer-muted: #9fc2e6;
    --white: #ffffff;
    --header-top: #ffffff;
    --header-bottom: #e9f2f8;
  }
  * { box-sizing: border-box; margin: 0; padding: 0; }
  html, body { width: 1200px; height: 942px; overflow: hidden; background: var(--white); }
  body { position: relative; font-family: "Arimo", Arial, sans-serif; }

  .site-header {
    position: absolute; left: 0; top: 0; width: 1200px; height: 98px;
    background: linear-gradient(var(--header-top), var(--header-bottom));
    border-bottom: 3px solid var(--brand-blue);
  }
  .brand {
    position: absolute; left: 24px; top: 30px;
    display: flex; align-items: center; gap: 10px;
    font-family: "Oswald", sans-serif; font-weight: 400; font-size: 26px;
    color: var(--navy);
  }
  .brand-mark { width: 26px; height: 26px; border-radius: 50%; background: var(--navy); }

  .main-nav { position: absolute; left: 312px; top: 39px; display: flex; }
  .main-nav a {
    display: block; height: 59px; line-height: 56px;
    padding: 0 26px; margin-right: 8px;
    font-family: "Oswald", sans-serif; font-weight: 300; font-size: 32px;
    color: var(--navy-dark); text-decoration: none;
  }
  .main-nav a.is-active {
    background: var(--brand-blue); color: var(--white);
    border-radius: 8px 8px 0 0; padding: 0 30px;
  }

  .hero {
    position: absolute; left: 0; top: 98px; width: 1200px; height: 371px;
    background: linear-gradient(90deg, var(--brand-blue-light), var(--brand-blue) 55%, var(--brand-blue-deep));
  }
  .hero-photo {
    position: absolute; left: 43px; top: 17px; width: 324px; height: 354px;
    background: linear-gradient(180deg, #d9e6ef, #9fc4dc 60%, #3fb0dc);
    border-radius: 140px 140px 0 0;
  }
  .hero-copy { position: absolute; left: 535px; top: 72px; width: 600px; color: var(--white); }
  .hero-title {
    font-family: "Oswald", sans-serif; font-weight: 700; font-size: 60px;
    line-height: 1; letter-spacing: -0.5px;
  }
  .hero-text {
    margin-top: 18px;
    font-family: "Oswald", sans-serif; font-weight: 300; font-size: 43px; line-height: 1.03;
  }
  .slider-dots { position: absolute; left: 1046px; top: 326px; display: flex; gap: 20px; }
  .slider-dots span { width: 28px; height: 28px; border-radius: 50%; background: var(--navy); }
  .slider-dots span.is-current { background: var(--white); }

  .hero-shadow {
    position: absolute; left: 0; top: 469px; width: 1200px; height: 34px;
    background: linear-gradient(#e6eff5, var(--white));
  }

  .devices {
    position: absolute; left: 55px; top: 520px; width: 398px; height: 325px;
    background: linear-gradient(135deg, #2a2a2a, #555 40%, #2fa7dc 60%, #e9f1f6);
    border-radius: 22px;
  }

  .solution { position: absolute; left: 585px; width: 585px; }
  .solution--link { top: 520px; }
  .solution--circles { top: 690px; }
  .solution-title {
    font-family: "Oswald", sans-serif; font-size: 38px; line-height: 1.1;
    color: var(--navy); font-weight: 700;
  }
  .solution-title .light { font-weight: 300; color: var(--title-light); }
  .solution-text { margin-top: 6px; font-size: 15px; line-height: 1.22; color: var(--text-blue); }
  .learn-more {
    display: inline-flex; align-items: center; gap: 8px;
    margin-top: 6px; width: 127px; height: 17px; padding-left: 14px;
    background: var(--navy); border-radius: 9px;
    font-size: 12px; font-weight: 700; color: var(--white); text-decoration: none;
  }

  .site-footer {
    position: absolute; left: 0; top: 867px; width: 1200px; height: 75px;
    background: var(--footer-bg); text-align: center;
  }
  .footer-nav { padding-top: 21px; font-size: 15px; }
  .footer-nav a { color: var(--footer-link); text-decoration: none; margin: 0 2px; }
  .copyright { margin-top: 5px; font-size: 12px; color: var(--footer-muted); }
  .social { position: absolute; left: 1009px; top: 23px; display: flex; gap: 9px; }
  .social span {
    width: 34px; height: 34px; background: #5a8ec4;
    display: flex; align-items: center; justify-content: center;
  }
</style>
</head>
<body>
  <header class="site-header">
    <div class="brand"><span class="brand-mark"></span>BrightvaleCare</div>
    <nav class="main-nav">
      <a class="is-active" href="#">HOME</a>
      <a href="#">ABOUT US</a>
      <a href="#">SOLUTIONS</a>
      <a href="#">PLATFORM MODEL</a>
      <a href="#">CONTACT US</a>
    </nav>
  </header>

  <section class="hero">
    <div class="hero-photo" role="img" aria-label="Photo of a doctor with a stethoscope using a smartphone"></div>
    <div class="hero-copy">
      <h1 class="hero-title">Improve Communication</h1>
      <p class="hero-text">Communication between the patient, the health care team, and the family care team</p>
    </div>
    <div class="slider-dots"><span class="is-current"></span><span></span><span></span></div>
  </section>
  <div class="hero-shadow"></div>

  <div class="devices" role="img" aria-label="Tablet and smartphone showing the BrightvaleCare home page"></div>

  <article class="solution solution--link">
    <h2 class="solution-title"><span class="light">Brightvale</span>ConnectLink</h2>
    <p class="solution-text">BCL offers Improve communication between the patient, the health care team, and the family care team", "Improve communication between Health Team members", and "Monitor for success and improvement opportunities of administrative goals using direct patient feedback.</p>
    <a class="learn-more" href="#">
      <svg width="20" height="9" viewBox="0 0 20 9"><path d="M0 4.5h14M10 1l5 3.5-5 3.5" stroke="#fff" stroke-width="2" fill="none"/></svg>learn more</a>
  </article>

  <article class="solution solution--circles">
    <h2 class="solution-title"><span class="light">Brightvale</span>Circles</h2>
    <p class="solution-text">Transition support to the Family Care Team", "Stay connected after discharge by creating a VitaCircle of support", and "Monitor progress, provide encouragement, and coordinate support of loved ones</p>
    <a class="learn-more" href="#">
      <svg width="20" height="9" viewBox="0 0 20 9"><path d="M0 4.5h14M10 1l5 3.5-5 3.5" stroke="#fff" stroke-width="2" fill="none"/></svg>learn more</a>
  </article>

  <footer class="site-footer">
    <nav class="footer-nav">
      <a href="#">HOME</a> <a href="#">ABOUT US</a> <a href="#">SOLUTIONS</a> <a href="#">PLATFORM MODEL</a> <a href="#">CONTACT US</a>
    </nav>
    <p class="copyright">Copyright © 2013 BrightvaleCare. All rights reserved.</p>
    <div class="social">
      <span aria-label="Email">
        <svg width="22" height="16" viewBox="0 0 22 16"><rect x="1" y="1" width="20" height="14" fill="none" stroke="#fff" stroke-width="2"/><path d="M1 1l10 8 10-8" fill="none" stroke="#fff" stroke-width="2"/></svg>
      </span>
      <span aria-label="Social link"></span>
      <span aria-label="Social link"></span>
      <span aria-label="Video link"></span>
    </div>
  </footer>
</body>
</html>
```